Just upload my Logo
Simple
Elsa Marroquín
quillmarshimages@postnook.net
Follow me in Chatterloom
* Wedding
* Engagment
* Maternity
* Newborn
* Family
* Events......etc

```html
<!DOCTYPE html>
<html lang="en">
<head>
<meta charset="utf-8">
<title>Elsa Marroquín — Business Card</title>
<link rel="stylesheet" href="https://fonts.googleapis.com/css2?family=Tinos:wght@400;700&display=swap">
<style>
  :root {
    --backdrop: #e9e9e9;
    --card: #ffffff;
    --aperture-light: #ececec;
    --aperture-mid: #dcdcdc;
    --ink: #2b2b2b;
    --ink-soft: #555555;
    --accent: #d9407c;
  }
  * { margin: 0; padding: 0; box-sizing: border-box; }
  html, body {
    width: 1200px;
    height: 1050px;
    overflow: hidden;
    background: var(--backdrop);
  }
  .canvas {
    position: relative;
    width: 1200px;
    height: 1050px;
  }
  .business-card {
    position: absolute;
    left: 100px;
    top: 240px;
    width: 1000px;
    height: 572px;
    background: var(--card);
    border-radius: 40px;
    overflow: hidden;
    box-shadow: 0 10px 30px rgba(0,0,0,0.18);
    font-family: "Tinos", "Times New Roman", serif;
  }
  .aperture-decoration {
    position: absolute;
    left: -190px;
    top: 20px;
    width: 420px;
    height: 420px;
    border-radius: 50%;
    background: radial-gradient(circle at 60% 45%, var(--aperture-light) 0%, var(--aperture-mid) 100%);
  }
  .brand-name {
    position: absolute;
    right: 80px;
    top: 120px;
    display: flex;
    align-items: center;
    gap: 16px;
    color: var(--accent);
    font-size: 42px;
    font-weight: 400;
    letter-spacing: 2px;
    white-space: nowrap;
  }
  .brand-dot {
    width: 18px;
    height: 18px;
    border-radius: 50%;
    background: var(--accent);
  }
  .holder-name {
    position: absolute;
    left: 70px;
    top: 352px;
    font-size: 46px;
    font-weight: 700;
    color: var(--ink);
  }
  .contact-list {
    position: absolute;
    left: 70px;
    top: 428px;
    list-style: none;
  }
  .contact-item {
    display: flex;
    align-items: center;
    gap: 14px;
    font-size: 26px;
    color: var(--ink-soft);
    margin-bottom: 12px;
  }
  .contact-icon {
    width: 26px;
    height: 26px;
    flex: none;
  }
</style>
</head>
<body>
<main class="canvas">
  <section class="business-card">
    <div class="aperture-decoration" role="img" aria-label="Large faint camera shutter aperture decoration"></div>

    <div class="brand-name">
      <span class="brand-dot"></span>
      <span>Quillmarsh Images</span>
    </div>

    <h1 class="holder-name">Elsa Marroquín</h1>
    <ul class="contact-list">
      <li class="contact-item">
        <svg class="contact-icon" viewBox="0 0 24 24" aria-hidden="true">
          <rect x="6" y="2" width="12" height="20" rx="2.5" fill="none" stroke="var(--accent)" stroke-width="2"/>
          <circle cx="12" cy="18" r="1.3" fill="var(--accent)"/>
        </svg>
        <span>(555) 014-2290</span>
      </li>
      <li class="contact-item">
        <svg class="contact-icon" viewBox="0 0 24 24" aria-hidden="true">
          <circle cx="12" cy="12" r="4" fill="none" stroke="var(--accent)" stroke-width="2"/>
          <path d="M16 8 v5 a2.5 2.5 0 0 0 5 0 v-1 a9 9 0 1 0 -4 7.5" fill="none" stroke="var(--accent)" stroke-width="2"/>
        </svg>
        <span>quillmarshimages@postnook.net</span>
      </li>
    </ul>
  </section>
</main>
</body>
</html>
```